make a logo presentation template - make a business branding template

1-i want the template to be used as a backbone where we put the logos and artwork in them
2-check the attached
3-we want a more pro design so you can do it from scratch
4-in the logo presentation for example - color scheme - place for description etc
5-in the business presentation we need to do for each category: id -business cards 3 designs - brochure -mockup - envelope - invoice - receipt - cd -email signature - a template that we can fill using photoshop or illustrator where we change only the colors and names and info and we get it done

```html
<!DOCTYPE html>
<html lang="en">
<head>
<meta charset="utf-8">
<title>Brand Presentation Template</title>
<link rel="stylesheet" href="https://fonts.googleapis.com/css2?family=Roboto+Slab:wght@400;700;800;900&display=swap">
<style>
  :root {
    --ink: #111111;
    --bg: #000000;
    --band: #fb8c69;
    --paper: #ffffff;
    --salmon: #f29878;
    --charcoal: #3a3131;
    --offwhite: #f7f7f7;
    --coral: #fd8c68;
    --peach: #fcb39b;
    --logo-fill: #f0906f;
    --sand: #c89d6b;
    --taupe: #c19e82;
    --sand-text: #c9996d;
    --brand-red: #8c1b22;
    --rule: #aaaaaa;
    --line: #bdbdbd;
  }
  * { box-sizing: border-box; margin: 0; padding: 0; }
  html, body { width: 1200px; height: 2455px; overflow: hidden; background: var(--bg); }
  body { font-family: "Roboto Slab", Georgia, serif; color: var(--ink); }
  .canvas { position: relative; width: 1200px; height: 2455px; overflow: hidden; background: var(--bg); }
  .bands { position: absolute; inset: 0; width: 1200px; height: 2455px; }
  .panel { position: absolute; background: var(--paper); }
  .panel-title { font-weight: 800; font-size: 19px; letter-spacing: 0.01em; position: absolute; }

  /* cover */
  .cover { left: 83px; top: 48px; width: 508px; height: 285px; }
  .brand-mark { position: absolute; left: 0; width: 100%; top: 165px; display: flex; justify-content: center; align-items: center; gap: 10px; }
  .brand-mark .square { width: 30px; height: 30px; background: var(--brand-red); }
  .brand-mark .name { font-weight: 700; font-size: 24px; letter-spacing: 0.08em; color: var(--brand-red); }
  .cover .eyebrow { position: absolute; top: 210px; width: 100%; text-align: center; font-size: 14px; letter-spacing: 0.14em; }
  .cover .client { position: absolute; top: 233px; width: 100%; text-align: center; font-size: 15px; font-weight: 700; color: var(--coral); }

  /* intro */
  .intro { left: 609px; top: 48px; width: 510px; height: 285px; }
  .intro .panel-title { left: 86px; top: 22px; }
  .intro .copy { position: absolute; left: 86px; top: 68px; width: 336px; font-size: 14px; line-height: 19px; text-align: justify; color: #333; }

  /* colours */
  .palette { left: 85px; top: 355px; width: 511px; height: 287px; }
  .palette .panel-title { left: 83px; top: 22px; }
  .swatch { position: absolute; width: 76px; height: 76px; }
  .swatch.salmon { left: 86px; top: 90px; background: var(--salmon); }
  .swatch.charcoal { left: 174px; top: 90px; background: var(--charcoal); }
  .swatch.offwhite { left: 262px; top: 90px; background: var(--offwhite); }
  .swatch.coral { left: 350px; top: 90px; background: var(--coral); }
  .swatch.peach { left: 86px; top: 177px; background: var(--peach); }

  /* typography */
  .type { left: 611px; top: 355px; width: 511px; height: 287px; }
  .specimen { position: absolute; font-size: 36px; line-height: 1; }
  .specimen.regular { left: 84px; top: 58px; font-weight: 400; }
  .specimen.bold { left: 380px; top: 178px; font-weight: 800; font-size: 34px; }
  .font-label { position: absolute; font-size: 10px; }
  .font-label.one { left: 84px; top: 112px; }
  .font-label.two { left: 383px; top: 223px; }
  .glyphs { position: absolute; left: 150px; width: 194px; font-size: 11px; line-height: 17.5px; color: #444; }
  .glyphs.one { top: 31px; }
  .glyphs.two { top: 151px; font-weight: 700; color: #222; }
  .glyphs .row { display: flex; justify-content: space-between; }

  /* logos */
  .logos { left: 88px; top: 657px; width: 1029px; height: 579px; }
  .logos .panel-title { left: 80px; top: 54px; }
  .logo-tile { position: absolute; display: flex; flex-direction: column; align-items: center; justify-content: center; text-align: center; box-shadow: 3px 4px 8px rgba(0,0,0,0.35); }
  .logo-tile .word { font-weight: 900; text-transform: uppercase; letter-spacing: 0.16em; line-height: 1.18; }
  .logo-tile .tag { font-weight: 800; letter-spacing: 0.22em; text-transform: uppercase; }
  .logo-tile.primary { left: 97px; top: 140px; width: 370px; height: 370px; border: 13px solid #1c1c1c; background: var(--logo-fill); }
  .logo-tile.primary .word { font-size: 46px; margin-top: 20px; }
  .logo-tile.primary .tag { font-size: 15px; margin-top: 62px; }
  .logo-tile.small { width: 183px; height: 184px; border-width: 6px; border-style: solid; }
  .logo-tile.small .word { font-size: 23px; margin-top: 6px; }
  .logo-tile.small .tag { font-size: 8px; margin-top: 24px; }
  .logo-tile.dark { left: 552px; top: 128px; background: #000; border-color: var(--coral); color: var(--coral); }
  .logo-tile.bright { left: 757px; top: 131px; background: var(--coral); border-color: #1c1c1c; }
  .logo-tile.light { left: 552px; top: 338px; background: var(--paper); border-color: #1c1c1c; }

  /* business cards */
  .cards { left: 85px; top: 1252px; width: 1029px; height: 579px; }
  .cards .panel-title { left: 83px; top: 66px; }
  .card { position: absolute; width: 242px; height: 150px; display: flex; align-items: center; justify-content: center; text-align: center; font-weight: 800; font-size: 15px; line-height: 19px; text-transform: uppercase; box-shadow: 0 2px 8px rgba(0,0,0,0.12); }
  .card.front { top: 163px; color: #fff; }
  .card.back { top: 352px; background: var(--paper); }
  .card.c1 { left: 100px; }
  .card.c2 { left: 395px; }
  .card.c3 { left: 688px; }
  .card.front.c1 { background: var(--charcoal); }
  .card.front.c2 { background: var(--sand); }
  .card.front.c3 { background: var(--taupe); }
  .card.back.c1 { color: #222; }
  .card.back.c2, .card.back.c3 { color: var(--sand-text); }

  /* letterhead */
  .letterhead { left: 85px; top: 1849px; width: 1029px; height: 579px; }
  .letterhead .panel-title { left: 83px; top: 57px; }
  .sheet { position: absolute; top: 130px; width: 262px; height: 385px; border: 3px solid var(--rule); background: var(--paper); }
  .sheet.cover-sheet { left: 240px; }
  .sheet.body-sheet { left: 548px; }
  .sheet .logo-tile { box-shadow: none; background: var(--logo-fill); border: 4px solid #1c1c1c; }
  .sheet .logo-tile.center { left: 52px; top: 112px; width: 153px; height: 155px; }
  .sheet .logo-tile.center .word { font-size: 18px; margin-top: 8px; }
  .sheet .logo-tile.center .tag { font-size: 6px; margin-top: 16px; }
  .sheet .logo-tile.corner { left: 25px; top: 24px; width: 57px; height: 58px; border-width: 2px; }
  .sheet .logo-tile.corner .word { font-size: 7px; letter-spacing: 0.1em; }
  .sheet .logo-tile.corner .tag { font-size: 3px; margin-top: 4px; }
  .writing-lines { position: absolute; left: 12px; top: 133px; width: 231px; height: 230px; display: flex; flex-direction: column; justify-content: space-between; }
  .writing-lines span { display: block; height: 1px; background: var(--line); }

  .next-panel { left: 85px; top: 2447px; width: 1029px; height: 20px; }
</style>
</head>
<body>
<div class="canvas">
  <svg class="bands" viewBox="0 0 900 1841" preserveAspectRatio="none" aria-hidden="true">
    <polygon points="585,0 830,0 0,830 0,585" fill="var(--band)"/>
    <polygon points="0,683 900,1133 900,1340 0,831" fill="var(--band)"/>
    <polygon points="0,1340 900,1841 540,1841 0,1530" fill="var(--band)"/>
  </svg>

  <section class="panel cover">
    <div class="brand-mark"><span class="square"></span><span class="name">NORTHWIND STUDIO</span></div>
    <p class="eyebrow">PRESENTATION FOR</p>
    <p class="client">“REPLACE WITH CLIENT NAME”</p>
  </section>

  <section class="panel intro">
    <h2 class="panel-title">INTRODUCTION</h2>
    <p class="copy">Describe Brand. Font Maintained with that used in logo template.<br>Lorem ipsum dolor sit amet, consectetur adipisicing elit, sed do eiusmod tempor incididunt ut labore et dolore error sit voluptatem accusantium explicabo. consectetur, adipisci velit, sed quia non numquam eius modi tempora quaerat voluptatem.</p>
  </section>

  <section class="panel palette">
    <h2 class="panel-title">BRAND COLOURS &amp; TYPOGRAPHY</h2>
    <div class="swatch salmon"></div>
    <div class="swatch charcoal"></div>
    <div class="swatch offwhite"></div>
    <div class="swatch coral"></div>
    <div class="swatch peach"></div>
  </section>

  <section class="panel type">
    <div class="specimen regular">Aa</div>
    <div class="font-label one">FONT 1</div>
    <div class="glyphs one">
      <div class="row"><span>A</span><span>B</span><span>C</span><span>D</span><span>E</span><span>F</span><span>G</span><span>H</span><span>I</span><span>J</span></div>
      <div class="row"><span>K</span><span>L</span><span>M</span><span>N</span><span>O</span><span>P</span><span>Q</span><span>R</span><span>S</span><span>T</span></div>
      <div class="row"><span>U</span><span>V</span><span>W</span><span>X</span><span>Y</span><span>Z</span><span>a</span><span>b</span><span>c</span><span>d</span></div>
      <div class="row"><span>e</span><span>f</span><span>g</span><span>h</span><span>i</span><span>j</span><span>k</span><span>l</span><span>m</span><span>n</span><span>o</span></div>
      <div class="row"><span>p</span><span>q</span><span>r</span><span>s</span><span>t</span><span>u</span><span>v</span><span>w</span><span>x</span><span>y</span><span>z</span></div>
      <div class="row"><span>0</span><span>1</span><span>2</span><span>3</span><span>4</span><span>5</span><span>6</span><span>7</span><span>8</span><span>9</span></div>
    </div>
    <div class="glyphs two">
      <div class="row"><span>A</span><span>B</span><span>C</span><span>D</span><span>E</span><span>F</span><span>G</span><span>H</span><span>I</span><span>J</span></div>
      <div class="row"><span>K</span><span>L</span><span>M</span><span>N</span><span>O</span><span>P</span><span>Q</span><span>R</span><span>S</span><span>T</span></div>
      <div class="row"><span>U</span><span>V</span><span>W</span><span>X</span><span>Y</span><span>Z</span><span>a</span><span>b</span><span>c</span><span>d</span></div>
      <div class="row"><span>e</span><span>f</span><span>g</span><span>h</span><span>i</span><span>j</span><span>k</span><span>l</span><span>m</span><span>n</span><span>o</span></div>
      <div class="row"><span>p</span><span>q</span><span>r</span><span>s</span><span>t</span><span>u</span><span>v</span><span>w</span><span>x</span><span>y</span><span>z</span></div>
      <div class="row"><span>0</span><span>1</span><span>2</span><span>3</span><span>4</span><span>5</span><span>6</span><span>7</span><span>8</span><span>9</span></div>
    </div>
    <div class="specimen bold">Aa</div>
    <div class="font-label two">FONT 2</div>
  </section>

  <section class="panel logos">
    <h2 class="panel-title">LOGOS &amp; ALTERNATIVE VERSIONS</h2>
    <div class="logo-tile primary"><div class="word">Replace<br>With<br>Logo</div><div class="tag">Colour 1</div></div>
    <div class="logo-tile small dark"><div class="word">Replace<br>With<br>Logo</div><div class="tag">Colour 2</div></div>
    <div class="logo-tile small bright"><div class="word">Replace<br>With<br>Logo</div><div class="tag">Colour 4</div></div>
    <div class="logo-tile small light"><div class="word">Replace<br>With<br>Logo</div><div class="tag">Colour 3</div></div>
  </section>

  <section class="panel cards">
    <h2 class="panel-title">BUSINESS CARDS</h2>
    <div class="card front c1">Replace with<br>business card<br>design 1 - front</div>
    <div class="card front c2">Replace with<br>business card<br>design 2 - front</div>
    <div class="card front c3">Replace with<br>business card<br>design 3 - front</div>
    <div class="card back c1">Replace with<br>business card<br>design 1 - back</div>
    <div class="card back c2">Replace with<br>business card<br>design 2 - back</div>
    <div class="card back c3">Replace with<br>business card<br>design 3- back</div>
  </section>

  <section class="panel letterhead">
    <h2 class="panel-title">LETTERHEAD</h2>
    <div class="sheet cover-sheet">
      <div class="logo-tile center"><div class="word">Replace<br>With<br>Logo</div><div class="tag">Colour 1</div></div>
    </div>
    <div class="sheet body-sheet">
      <div class="logo-tile corner"><div class="word">Replace<br>With<br>Logo</div><div class="tag">Colour 1</div></div>
      <div class="writing-lines">
        <span></span><span></span><span></span><span></span><span></span><span></span><span></span><span></span><span></span><span></span><span></span>
      </div>
    </div>
  </section>

  <section class="panel next-panel"></section>
</div>
</body>
</html>
```